BQL Groundworks & Freight Business Card

Can you please design a business card for an Earthworks, Haulage truck and machinery hire company. They also provide sand soil and mulch supply, as well as screening of products. Can you re-create the logo from the attached but add BQL Groundworks & Freight just use the three diamond design.

Target Market(s)

Earthmoving and Transport, Landscapers, Construction

Contact Information for Business Card

ABN 52 907 334 816, Doug Pelham, Managing Director, BQL Groundworks & Freight Mobile 0438 256 904 Email bqlfreight2010@mailvane.net

Font styles to use
Sans Serif

Colors
ec1f27
000000
cbcbcb
ffffff

Requirements
Must have
• Listed on the back, Earthworks | Haulage | Truck and Machinery Hire | Sand, Soil & Mulch Supply | Screening of Products
Nice to have
• Would be good for it to look appealing to a mans man, because it relates to heavy machinery, earthworks, construction etc. Black, red and white would be good maybe with a bit of silver somewhere.
Should not have
• not sure

```html
<!DOCTYPE html>
<html lang="en">
<head>
<meta charset="utf-8">
<title>BQL Groundworks &amp; Freight – Business Card</title>
<link href="https://fonts.googleapis.com/css2?family=Roboto:ital,wght@0,300;0,400;0,500;0,700;1,300;1,700&display=swap" rel="stylesheet">
<style>
  :root {
    --red: #ec1f27;
    --black: #000000;
    --silver: #cbcbcb;
    --white: #ffffff;
    --ink: #231f20;
  }
  html, body {
    margin: 0;
    padding: 0;
    width: 1200px;
    height: 1200px;
    overflow: hidden;
    background: var(--white);
    font-family: "Roboto", Arial, sans-serif;
  }
  .canvas { position: relative; width: 1200px; height: 1200px; }

  .card { position: absolute; width: 842px; height: 480px; border-radius: 32px; overflow: hidden; }
  .card-front { left: 60px; top: 62px; }
  .card-back { left: 292px; top: 654px; box-shadow: inset 0 0 0 1px #333; }
  .card-bg { position: absolute; inset: 0; }

  .contact { position: absolute; right: 34px; text-align: right; color: var(--white); white-space: nowrap; }
  .contact-name { top: 40px; font-size: 36px; font-weight: 500; font-variant: small-caps; letter-spacing: 3px; line-height: 1; }
  .contact-title { top: 84px; font-size: 26px; font-weight: 400; line-height: 1; }
  .contact-line { font-size: 26px; font-weight: 300; line-height: 1; display: flex; align-items: center; gap: 12px; justify-content: flex-end; }
  .contact-phone { top: 128px; }
  .contact-email { top: 168px; }
  .contact-line svg { width: 24px; height: 24px; fill: var(--white); }
  .contact-abn { top: 476px; font-size: 37px; font-weight: 400; line-height: 1; transform: translateY(-100%); }

  .brand-box { position: absolute; left: 51px; top: 136px; width: 279px; height: 181px; background: var(--white); }
  .brand-name { position: absolute; left: 0; right: 0; top: 30px; display: flex; align-items: center; justify-content: center; gap: 12px; font-size: 62px; font-weight: 700; color: var(--black); line-height: 1; }
  .brand-mark { width: 22px; height: 22px; background: var(--red); }
  .brand-sub { position: absolute; left: 0; right: 0; top: 110px; text-align: center; font-size: 18px; font-weight: 700; color: var(--ink); }
  .brand-phone { position: absolute; left: 0; right: 0; top: 142px; text-align: center; font-size: 30px; font-weight: 700; color: var(--ink); line-height: 1; }
  .tagline { position: absolute; left: 51px; width: 279px; top: 320px; text-align: center; font-size: 19px; font-style: italic; font-weight: 300; letter-spacing: 1px; color: var(--white); }

  .services-heading { position: absolute; left: 80px; top: 428px; font-size: 35px; font-weight: 700; font-style: italic; color: var(--ink); line-height: 1; }
  .service { position: absolute; font-size: 35px; font-weight: 700; font-style: italic; color: var(--ink); line-height: 1; white-space: nowrap; }
</style>
</head>
<body>
<div class="canvas">

  <section class="card card-front">
    <svg class="card-bg" width="842" height="480" viewBox="0 0 842 480" aria-hidden="true">
      <defs>
        <radialGradient id="redGlow" cx="110" cy="240" r="330" gradientUnits="userSpaceOnUse">
          <stop offset="0" stop-color="#ec1f27"/>
          <stop offset="0.42" stop-color="#ec1f27"/>
          <stop offset="0.78" stop-color="#7a0d12"/>
          <stop offset="1" stop-color="#000"/>
        </radialGradient>
        <linearGradient id="silverFront" x1="0" y1="0" x2="1" y2="0">
          <stop offset="0" stop-color="#555"/>
          <stop offset="0.6" stop-color="#ddd"/>
          <stop offset="1" stop-color="#fff"/>
        </linearGradient>
      </defs>
      <rect width="842" height="480" fill="url(#redGlow)"/>
      <path d="M272 0 Q552 240 272 480 L842 480 L842 0 Z" fill="#000"/>
      <path d="M272 0 Q552 240 272 480 Q520 240 272 0 Z" fill="url(#silverFront)"/>
    </svg>

    <div class="brand-box">
      <div class="brand-name"><span class="brand-mark"></span>BQL</div>
      <div class="brand-sub">Groundworks &amp; Freight</div>
      <div class="brand-phone">0438 256 904</div>
    </div>
    <div class="tagline">for all your transport needs</div>

    <div class="contact contact-name">Doug Pelham</div>
    <div class="contact contact-title">Managing Director</div>
    <div class="contact contact-line contact-phone">0438 256 904
      <svg viewBox="0 0 24 24"><path d="M6.6 10.8c1.4 2.8 3.8 5.1 6.6 6.6l2.2-2.2c.3-.3.7-.4 1-.2 1.1.4 2.3.6 3.6.6.6 0 1 .4 1 1V20c0 .6-.4 1-1 1C10.6 21 3 13.4 3 4c0-.6.4-1 1-1h3.5c.6 0 1 .4 1 1 0 1.3.2 2.5.6 3.6.1.3 0 .7-.2 1L6.6 10.8z"/></svg>
    </div>
    <div class="contact contact-line contact-email">bqlfreight2010@mailvane.net
      <svg viewBox="0 0 24 24"><path d="M22 2 2 10l7 3 2 8 3-6 5 4z"/></svg>
    </div>
    <div class="contact contact-abn">ABN: 52 907 334 816</div>
  </section>

  <section class="card card-back">
    <svg class="card-bg" width="842" height="480" viewBox="0 0 842 480" aria-hidden="true">
      <defs>
        <linearGradient id="silverBack" x1="0" y1="0" x2="1" y2="0">
          <stop offset="0" stop-color="#999"/>
          <stop offset="0.7" stop-color="#eee"/>
          <stop offset="1" stop-color="#fff"/>
        </linearGradient>
      </defs>
      <rect width="842" height="480" fill="#cbcbcb"/>
      <path d="M218 0 Q494 240 216 480 Q460 240 218 0 Z" fill="url(#silverBack)"/>
    </svg>

    <div class="services-heading">Our Services</div>
    <div class="service" style="left:362px;top:96px;">Truck and Machinery Hire</div>
    <div class="service" style="left:380px;top:160px;">Earthworks</div>
    <div class="service" style="left:386px;top:224px;">Haulage</div>
    <div class="service" style="left:375px;top:288px;">Sand, Soil &amp; Mulch Supply</div>
    <div class="service" style="left:348px;top:352px;">Screening of Products</div>
  </section>

</div>
</body>
</html>
```